Clinical Layout Builders - Stationery
Biz Cards + Stationary
Clinical Layout Builders - Stationery - Information Technology
Creative Brief
Professional
Dr. Elena M. Castillo
Director of Content Development
Ceiba Business Plaza #3, Suite 118 San Juan, PR 00941
(787) PENDING
elena.castillo@hnvwqbt.com
www.hnvwqbt.com
Need a second set of cards for: Dr. Luis F. Beltran Business Development Director Same info- address, fax and phone (Pending) Cell: (787) 555-0192 Email: luis.beltran@hnvwqbt.com
Either the logo, the website or something else. Feel free to be creative!

```html
<!DOCTYPE html>
<html lang="en">
<head>
<meta charset="utf-8">
<title>Clinical Layout Builders – Business Cards</title>
<link href="https://fonts.googleapis.com/css2?family=Open+Sans:wght@400;600;700&display=swap" rel="stylesheet">
<style>
  :root {
    --page-bg: #f2f2f2;
    --magenta: #9b1d6b;
    --magenta-dark: #6a0f47;
    --magenta-light: #c14a8f;
    --card-white: #ffffff;
    --swoosh-grey: #9a9a9a;
    --text-light: #ffffff;
    --text-soft: #f3d9e8;
  }
  * { margin: 0; padding: 0; box-sizing: border-box; }
  html, body {
    width: 1200px; height: 949px; overflow: hidden;
    background: var(--page-bg);
    font-family: "Open Sans", sans-serif;
  }
  .stage { position: relative; width: 1200px; height: 949px; }

  .card {
    position: absolute;
    width: 470px; height: 268px;
    border-radius: 14px;
    overflow: hidden;
    box-shadow: 0 4px 14px rgba(0,0,0,0.18);
  }

  /* Front card */
  .card-front { left: 300px; top: 210px; background: var(--card-white); }
  .card-front .card-art { position: absolute; inset: 0; }
  .brand-front {
    position: absolute; left: 34px; top: 34px;
    display: flex; align-items: center; gap: 10px;
    color: var(--magenta);
    font-weight: 700; font-size: 24px; letter-spacing: 0.5px;
  }
  .brand-mark { width: 16px; height: 16px; background: var(--magenta); }
  .holder {
    position: absolute; left: 30px; top: 170px;
    color: var(--text-light);
  }
  .holder-name { font-size: 13px; font-weight: 600; }
  .holder-title { font-size: 9.5px; color: var(--text-soft); margin-top: 2px; }
  .divider {
    position: absolute; left: 222px; top: 146px;
    width: 1px; height: 104px; background: rgba(255,255,255,0.7);
  }
  .contact {
    position: absolute; left: 232px; top: 146px;
    list-style: none;
    color: var(--text-light);
    font-size: 10px; line-height: 16.5px;
  }

  /* Back card */
  .card-back {
    left: 420px; top: 520px;
    background: radial-gradient(ellipse at 50% 35%, var(--magenta-light) 0%, var(--magenta) 45%, var(--magenta-dark) 100%);
  }
  .brand-back {
    position: absolute; left: 0; right: 0; top: 92px;
    display: flex; justify-content: center; align-items: center; gap: 12px;
    color: var(--text-light);
    font-weight: 700; font-size: 28px; letter-spacing: 0.5px;
  }
  .brand-back .brand-mark { background: var(--text-light); width: 18px; height: 18px; }
  .website {
    position: absolute; left: 0; right: 0; bottom: 30px;
    text-align: center;
    color: var(--text-light);
    font-size: 12px; letter-spacing: 3px;
  }
</style>
</head>
<body>
<main class="stage">

  <section class="card card-front" aria-label="Business card front">
    <svg class="card-art" width="470" height="268" viewBox="0 0 470 268" aria-hidden="true">
      <defs>
        <linearGradient id="frontBand" x1="0" y1="0" x2="0" y2="1">
          <stop offset="0" stop-color="#b23a80"/>
          <stop offset="0.5" stop-color="#9b1d6b"/>
          <stop offset="1" stop-color="#6a0f47"/>
        </linearGradient>
      </defs>
      <path d="M0 128 C140 128 300 112 470 76 L470 268 L0 268 Z" fill="url(#frontBand)"/>
      <path d="M0 116 C150 118 310 100 470 62" fill="none" stroke="#9a9a9a" stroke-width="5"/>
      <path d="M0 124 C150 126 310 108 470 70" fill="none" stroke="#d0d0d0" stroke-width="2"/>
    </svg>

    <div class="brand-front">
      <span class="brand-mark"></span>
      <span>Clinical Layout Builders</span>
    </div>

    <div class="holder">
      <p class="holder-name">Dr. Elena M. Castillo</p>
      <p class="holder-title">Director of Content Development</p>
    </div>

    <div class="divider"></div>

    <ul class="contact">
      <li>Ceiba Business Plaza #3, Suite 118</li>
      <li>San Juan, PR 00941</li>
      <li>Phone: (787) PENDING</li>
      <li>Cell: (787) 555-0176</li>
      <li>Fax: (787) 555-0148</li>
      <li>Email: elena.castillo@hnvwqbt.com</li>
    </ul>
  </section>

  <section class="card card-back" aria-label="Business card back">
    <div class="brand-back">
      <span class="brand-mark"></span>
      <span>Clinical Layout Builders</span>
    </div>
    <p class="website">www.hnvwqbt.com</p>
  </section>

</main>
</body>
</html>
```